We are a building company that build new homes and units we are looking for something fresh and looks good my company name is
Larkmoor Building Group Pty Ltd

Industry/Entity Type

Building

Contact Information for Business Card

Name Marco Delacruz-Fenn
Tittle: Director
Address 14 Quarrel St. Thornbury Vic 3071
Ph: 03 9612 4087
Mobile : 0400 562 938

www.larkmoorbuildinggroup.com.au
Email: sales@larkmoorbuildinggroup.com.au

```html
<!DOCTYPE html>
<html lang="en">
<head>
<meta charset="utf-8">
<title>Larkmoor Building Group – Business Card</title>
<link rel="stylesheet" href="https://fonts.googleapis.com/css2?family=Exo+2:wght@400;500;600;700&display=swap">
<style>
  :root {
    --backdrop: #ead4aa;
    --card: #000000;
    --red: #ee1c25;
    --white: #ffffff;
    --divider: #3a3a3a;
  }
  * { box-sizing: border-box; margin: 0; padding: 0; }
  html, body { width: 1189px; height: 1200px; overflow: hidden; }
  body {
    background: var(--backdrop);
    font-family: "Exo 2", sans-serif;
    position: relative;
  }
  .card {
    position: absolute;
    left: 171px;
    width: 856px;
    height: 487px;
    background: var(--card);
    border-radius: 23px;
    color: var(--white);
  }
  .card--front { top: 68px; }
  .card--back { top: 627px; }

  .wordmark {
    position: absolute;
    text-align: center;
    color: var(--red);
    font-weight: 700;
    line-height: 1;
    text-transform: uppercase;
  }
  .wordmark span { display: block; }
  .card--front .wordmark { left: 0; right: 0; top: 108px; }
  .card--front .wordmark__name { font-size: 80px; letter-spacing: 4px; }
  .card--front .wordmark__sub { font-size: 38px; margin-top: 14px; }
  .card--front .wordmark__tail { font-size: 36px; margin-top: 10px; }

  .front-web {
    position: absolute;
    left: 0; right: 0; top: 390px;
    text-align: center;
    font-size: 25px;
    font-weight: 500;
  }

  .card--back .wordmark { left: 60px; width: 276px; top: 170px; }
  .card--back .wordmark__name { font-size: 54px; letter-spacing: 2px; }
  .card--back .wordmark__sub { font-size: 26px; margin-top: 12px; }
  .card--back .wordmark__tail { font-size: 25px; margin-top: 8px; }

  .divider {
    position: absolute;
    left: 379px; top: 84px;
    width: 1px; height: 320px;
    background: var(--divider);
  }
  .person { position: absolute; left: 410px; top: 118px; }
  .person__name { color: var(--red); font-size: 36px; font-weight: 600; line-height: 1.1; }
  .person__title { font-size: 26px; font-weight: 400; line-height: 1.1; margin-top: 2px; }

  .contacts { position: absolute; left: 410px; top: 238px; list-style: none; }
  .contacts li {
    display: flex; align-items: center;
    height: 33px;
    font-size: 21px; font-weight: 500;
  }
  .contacts svg { width: 23px; height: 23px; margin-right: 10px; flex: none; }
</style>
</head>
<body>

<section class="card card--front">
  <div class="wordmark">
    <span class="wordmark__name">Larkmoor</span>
    <span class="wordmark__sub">Building Group</span>
    <span class="wordmark__tail">Pty Ltd</span>
  </div>
  <p class="front-web">www.larkmoorbuildinggroup.com.au</p>
</section>

<section class="card card--back">
  <div class="wordmark">
    <span class="wordmark__name">Larkmoor</span>
    <span class="wordmark__sub">Building Group</span>
    <span class="wordmark__tail">Pty Ltd</span>
  </div>
  <div class="divider"></div>
  <div class="person">
    <p class="person__name">Marco Delacruz-Fenn</p>
    <p class="person__title">Managing Director</p>
  </div>
  <ul class="contacts">
    <li>
      <svg viewBox="0 0 24 24" aria-hidden="true"><rect width="24" height="24" rx="4" fill="#ee1c25"/><rect x="8.5" y="4" width="7" height="16" rx="1.5" fill="none" stroke="#fff" stroke-width="1.6"/><rect x="10" y="6" width="4" height="5" fill="#fff"/></svg>
      0400 562 938
    </li>
    <li>
      <svg viewBox="0 0 24 24" aria-hidden="true"><rect width="24" height="24" rx="4" fill="#ee1c25"/><path d="M5 10c0-3 14-3 14 0v1.5h-3.5V9.5h-7v2H5z" fill="#fff"/><path d="M8 12h8l2 6H6z" fill="#fff"/></svg>
      03 9612 4087
    </li>
    <li>
      <svg viewBox="0 0 24 24" aria-hidden="true"><rect width="24" height="24" rx="4" fill="#ee1c25"/><rect x="5" y="7" width="14" height="10" fill="none" stroke="#fff" stroke-width="1.6"/><path d="M5 7l7 6 7-6M5 17l5-5M19 17l-5-5" fill="none" stroke="#fff" stroke-width="1.4"/></svg>
      sales@larkmoorbuildinggroup.com.au
    </li>
    <li>
      <svg viewBox="0 0 24 24" aria-hidden="true"><rect width="24" height="24" rx="4" fill="#ee1c25"/><g fill="none" stroke="#fff" stroke-width="1.3"><circle cx="12" cy="12" r="6.5"/><ellipse cx="12" cy="12" rx="3" ry="6.5"/><path d="M5.5 12h13M6.5 8.5h11M6.5 15.5h11"/></g></svg>
      www.larkmoorbuildinggroup.com.au
    </li>
  </ul>
</section>

</body>
</html>
```